Lena's Yuletide Album CD Art for Album Release Dec 14, 2017.

CD cover for Lena Hartwell's "Lena's Yuletide" Christmas music album. Must include hi-res photo and LH logo front and back, "Lena Hartwell", and "Lena's Yuletide". Also, please add "Vol 1" somewhere in the work and on the spine. Lena plans multiple albums of Christmas music in the coming years. CD design format templates attached to design to for production. If possible, consider some blank space on the CD and cover, so Lena can autograph same, when sold in person. Include the song listing and times of each song as seen on the attached word doc. Order pf artwork: 1) Front CD Cover with feature photo and album title; 2) Inside left with a few pics of Lena in the studio; 3) Back of CD case listing songs, contributors etc. Song listing info to follow, since we are in the studio now. Expecting 11 songs. I have uploaded the list to be placed on the back of the CD. I will have the times to fill in by then end of next week, since Lena is recording again on Tuesday Nov 21.
Updates

Need to add the UPC code to the lower back of the cd. UPC-A code is: 403186529074. Use this UPC label maker: https://www.tagprintbox.example/label-generator-tools/Barcode-Generator.aspx

Update #1 a) Please use script font for the album cover text. b) Remove the words "Lena Hartwell" off of the LH logo used on the front cover. c) Do not use photos from other album covers in the project. They are copyright protected by Tallow Records. They were provided as examples. d) You can get a flavor of LEna's work on the landing page of her website: www.lenahartwell.example, and the upcoming Christmas concert Thks, Dennis

Target Market(s)

Lena Hartwell fan base, and all Christmas music lovers.

Font styles to use
Script

Colors

Designer to choose colors to be used in the design.

Requirements
Must have
• Lena Hartwell's "Lena's Yuletide" Christmas music album. Must include hi-res photo and LH logo front and back, "Lena Hartwell", and "Lena's Yuletide". Also, please add "Vol 1" somewhere in the work and on the spine.
• A little Christmas art flare added.
Nice to have
• If possible, consider some blank space on the CD and cover, so Lena can autograph same, when sold in person.

```html
<!DOCTYPE html>
<html lang="en">
<head>
<meta charset="utf-8">
<title>Lena's Yuletide – Lena Hartwell Vol 1</title>
<link rel="stylesheet" href="https://fonts.googleapis.com/css2?family=Great+Vibes&family=Cinzel:wght@400&family=Roboto+Condensed:wght@300;700&display=swap">
<style>
  :root{
    --bg-deep:#1c0b04;
    --bg-warm:#5a2a0c;
    --gold:#e3b64a;
    --ink:#f4ece0;
    --ink-soft:#e2d6c6;
    --title-red:#d4141c;
    --hair:#0b0807;
    --skin:#8a5538;
    --skin-light:#a8714d;
  }
  *{margin:0;padding:0;box-sizing:border-box}
  html,body{width:1200px;height:571px;overflow:hidden;background:var(--bg-deep)}
  .sleeve{
    position:relative;width:1200px;height:571px;overflow:hidden;
    background:
      radial-gradient(circle at 8% 62%, rgba(200,121,31,.55) 0, transparent 22%),
      radial-gradient(circle at 30% 88%, rgba(214,140,40,.45) 0, transparent 20%),
      radial-gradient(circle at 48% 30%, rgba(150,80,25,.45) 0, transparent 24%),
      radial-gradient(circle at 66% 12%, rgba(230,170,70,.5) 0, transparent 14%),
      radial-gradient(circle at 62% 70%, rgba(170,90,25,.45) 0, transparent 20%),
      linear-gradient(180deg, var(--bg-warm) 0%, #3a1806 55%, var(--bg-deep) 100%);
    font-family:"Roboto Condensed", Arial, sans-serif;color:var(--ink);
  }
  /* back panel */
  .tracklist{position:absolute;left:26px;top:38px;width:530px;list-style:none;font-size:8.6px;line-height:11.4px;font-weight:300}
  .tracklist li{display:flex;margin-bottom:5.6px}
  .tracklist .num{width:15px;flex:none}
  .tracklist .title,.tracklist .credit{display:block}
  .tracklist .credit{color:var(--ink-soft)}
  .back-brand{position:absolute;left:250px;top:394px;width:70px;text-align:center}
  .back-brand .mark{width:50px;height:56px;margin:0 auto;border:2px solid var(--gold);display:flex;align-items:center;justify-content:center;
    font-family:"Cinzel", serif;font-size:20px;color:var(--gold)}
  .back-brand .name{margin:9px -30px 0;font-family:"Cinzel", serif;font-size:8px;color:var(--gold);white-space:nowrap}
  .credits{position:absolute;left:40px;top:482px;width:486px;text-align:center;font-size:8.8px;line-height:16px;font-weight:700}
  /* spine */
  .spine{position:absolute;left:556px;top:0;width:70px;height:571px;
    border-left:1px solid rgba(255,220,160,.12);border-right:1px solid rgba(255,220,160,.12)}
  .spine-title{position:absolute;left:35px;top:40px;transform-origin:0 0;transform:rotate(90deg) translateY(-50%);
    font-family:"Great Vibes", cursive;font-size:28px;color:var(--ink);white-space:nowrap}
  .spine-vol{position:absolute;left:0;width:70px;top:510px;text-align:center;font-family:"Cinzel", serif;color:var(--ink-soft);font-size:12px;line-height:14px}
  .spine-vol b{display:block;font-weight:400;font-size:24px;line-height:28px}
  /* front */
  .cover-photo{position:absolute;left:760px;top:0;width:440px;height:571px;
    background:
      radial-gradient(ellipse 30% 26% at 80% 34%, var(--skin-light) 0, var(--skin) 60%, transparent 100%),
      radial-gradient(ellipse 26% 16% at 78% 86%, var(--skin) 0, rgba(138,85,56,.7) 60%, transparent 100%),
      radial-gradient(ellipse 8% 30% at 60% 62%, rgba(227,182,74,.55) 0, transparent 100%),
      linear-gradient(90deg, transparent 0%, rgba(11,8,7,.75) 22%, var(--hair) 45%, #2a160c 75%, #3b2012 100%);
  }
  .album-title{position:absolute;left:640px;top:26px;width:380px;font-family:"Great Vibes", cursive;text-align:center;font-weight:400}
  .album-title .possessive{display:block;color:#fff;font-size:72px;line-height:74px;margin-left:120px}
  .album-title .season{display:block;color:var(--title-red);font-size:88px;line-height:80px;margin-top:-10px}
  .front-brand{position:absolute;left:784px;top:362px;width:86px;height:100px;border:2px solid var(--gold);
    display:flex;align-items:center;justify-content:center;font-family:"Cinzel", serif;font-size:32px;color:var(--gold)}
  .artist{position:absolute;left:678px;top:484px;font-family:"Cinzel", serif;font-size:40px;line-height:44px;color:#fff}
  .volume{position:absolute;left:680px;top:530px;font-family:"Cinzel", serif;font-size:21px;line-height:24px;color:#fff}
</style>
</head>
<body>
<main class="sleeve">
  <section class="back-panel">
    <ol class="tracklist">
      <li><span class="num">1.</span><span><span class="title">The First Noel (x:xx)</span><span class="credit">Music by Avery Dunmore, Lyrics by date back to 1823, in current form by composer Henry Lattimer, publish 1871.</span></span></li>
      <li><span class="num">2.</span><span><span class="title">Little Town of Bethlehem (x:xx)</span><span class="credit">Music by Avery Dunmore, Lyrics by Walter Pennick, published 1868.</span></span></li>
      <li><span class="num">3.</span><span><span class="title">Silent Night (x:xx)</span><span class="credit">Music by Avery Dunmore, Lyrics by Anton Weisel, composed by Karl Brenner, released 1818.</span></span></li>
      <li><span class="num">4.</span><span><span class="title">Joy to The World (x:xx)</span><span class="credit">Music by Avery Dunmore, Lyrics by Elias Thorne based on Psalm 98:11-12 and Genesis 3:17-18, published in 1719.</span></span></li>
      <li><span class="num">5.</span><span><span class="title">Oh Come, All Ye Faithful (x:xx)</span><span class="credit">Music by Avery Dunmore, Lyrics by dates back to 1600's; current version by Frederick Ashby published in 1841.</span></span></li>
      <li><span class="num">6.</span><span><span class="title">This Christmas (x:xx)</span><span class="credit">Music by Avery Dunmore, Lyrics by Nadia Rose Kinley &amp; Darnell Haskins, released 1970 and peaked #11 on<br>Chartline's Adult Contemporary chart, December 1972.</span></span></li>
      <li><span class="num">7.</span><span><span class="title">Have Yourself a Merry Little Christmas (x:xx)</span><span class="credit">Music by Avery Dunmore, Lyricas by Ralph Corwin, Composed by Hugh Merritt, Released 1944 introduced by Judy Carrow.</span></span></li>
      <li><span class="num">8.</span><span><span class="title">Little Drummer Boy (x:xx)</span><span class="credit">Music by Avery Dunmore &amp; Andreas Pryor, Lyrics by Katherine L. Dayle, released 1941.<br>Lou Rainer took it to #2 on Chartline magazine's special Christmas singles chart in 1967.</span></span></li>
      <li><span class="num">9.</span><span><span class="title">Oh Holy Night (x:xx)</span><span class="credit">Music by Avery Dunmore, Lyrics and composed by Adolphe Arnaud, 1847, first released recording by Enrico Valli, 1916.</span></span></li>
      <li><span class="num">10.</span><span><span class="title">Please Come Home For Christmas (x:xx)</span><span class="credit">Music by Derrick Fulton (KeyFlame), Lyrics by Charles Bowen &amp; Gene Reeves, released 1960 hitting Chartline Hot 100 in Dec 1961.</span></span></li>
      <li><span class="num">11.</span><span><span class="title">Lena Did You Know (x:xx)</span><span class="credit">Music by Avery Dunmore, Lyrics by Mark Lindell, composed by Buddy Grant.  Released 1992.</span></span></li>
    </ol>
    <div class="back-brand">
      <div class="mark">LH</div>
      <div class="name">LENA HARTWELL</div>
    </div>
    <div class="credits">
      <p>Recorded at: Bright Fern Studios, 2715 Cedarline Rd., Halverton, TX, 77950 www.brightfernstudio.example</p>
      <p>Produced by: Lena Hartwell, Ian Shelby &amp; Michael Tate (TopChordz)</p>
      <p>Executive Producer: Dennis Wolcott</p>
      <p>© 2017, Rosewood Entertainment, LLC, 48 Parkview PLZ, STE 900, Halverton, TX 77951</p>
      <p>www.lenahartwell.example • www.rosewoodentcorp.example</p>
    </div>
  </section>

  <section class="spine">
    <div class="spine-title">Lena's Yuletide</div>
    <div class="spine-vol">VOL<b>1</b></div>
  </section>

  <section class="front-panel">
    <div class="cover-photo" role="img" aria-label="Portrait photograph of Lena Hartwell smiling, with long flowing dark hair, gold drop earrings and a ring on her hand"></div>
    <h1 class="album-title"><span class="possessive">Lena's</span><span class="season">Yuletide</span></h1>
    <div class="front-brand">LH</div>
    <p class="artist">LENA HARTWELL</p>
    <p class="volume">VOL 1</p>
  </section>
</main>
</body>
</html>
```